Business Card Design Project

I have established a company called "Morrowvale" which is a business specialising in psychotherapy/counselling , predominantly for anxiety & depression.

My name is Tev....hence, the Morrowvale link. However, Morrowvale was also chosen for its reference to green shoots of growth/recovery.

Morrowvale is to be "upmarket" and highly professional. I'm keen for the style and colours to reflect this.....taupe/grey with navy/black script, for example.....NO primary colours.

My name needs to be on the card and my mobile number. Not sure, but suspect it should also have my qualifications ( BA (Psych) & BSc (Hons) Psychology). Mobile number 0491 627 850.

```html
<!DOCTYPE html>
<html lang="en">
<head>
<meta charset="utf-8">
<title>Morrowvale — Business Card, Front</title>
<link rel="stylesheet" href="https://fonts.googleapis.com/css2?family=Julius+Sans+One&family=Source+Sans+3:wght@400;600&display=swap">
<style>
  :root {
    --page-bg: #ecebea;
    --card-dark: #6c6d70;
    --card-mid: #828386;
    --card-light: #9a9b9e;
    --photo-light: #d4d4d4;
    --photo-mid: #a9a9a9;
    --photo-shade: #7d7d7d;
    --strip: #a4a5a8;
    --name-blue: #4a55ae;
    --brand-green: #a9c83c;
    --ink: #111111;
    --tagline: #f4f4f4;
  }
  * { box-sizing: border-box; margin: 0; padding: 0; }
  html, body {
    width: 1026px;
    height: 1200px;
    overflow: hidden;
    background: var(--page-bg);
  }
  .business-card {
    position: absolute;
    left: 63px;
    top: 351px;
    width: 900px;
    height: 497px;
    overflow: hidden;
    background: linear-gradient(100deg, var(--card-dark) 0%, var(--card-mid) 55%, var(--card-light) 100%);
    font-family: "Source Sans 3", "Myriad Pro", sans-serif;
  }
  .card-photo {
    position: absolute;
    left: 0;
    top: 0;
    width: 320px;
    height: 100%;
    background:
      radial-gradient(ellipse 70px 200px at 150px 250px, var(--photo-shade) 0%, rgba(125,125,125,0) 100%),
      linear-gradient(90deg, var(--photo-light) 0%, var(--photo-mid) 100%);
  }
  .card-strip {
    position: absolute;
    left: 320px;
    top: 0;
    width: 30px;
    height: 100%;
    background: linear-gradient(180deg, var(--strip), var(--card-light));
    opacity: 0.85;
  }
  .card-glow {
    position: absolute;
    left: 0;
    bottom: 0;
    width: 100%;
    height: 140px;
    background: linear-gradient(180deg, rgba(255,255,255,0) 0%, rgba(255,255,255,0.18) 100%);
  }
  .card-details {
    position: absolute;
    right: 58px;
    top: 0;
    text-align: right;
  }
  .holder-name {
    position: absolute;
    right: 0;
    top: 80px;
    font-family: "Julius Sans One", sans-serif;
    font-size: 96px;
    line-height: 1;
    color: var(--name-blue);
    letter-spacing: 1px;
    white-space: nowrap;
  }
  .brand-name {
    position: absolute;
    right: 0;
    top: 180px;
    font-size: 50px;
    line-height: 1;
    font-weight: 400;
    color: var(--brand-green);
    white-space: nowrap;
  }
  .credentials {
    position: absolute;
    right: 0;
    top: 244px;
    list-style: none;
    font-size: 31px;
    line-height: 40px;
    color: var(--ink);
    white-space: nowrap;
  }
  .tagline {
    position: absolute;
    right: 58px;
    top: 431px;
    font-size: 40px;
    line-height: 1;
    color: var(--tagline);
    white-space: nowrap;
  }
</style>
</head>
<body>
  <article class="business-card">
    <div class="card-photo" role="img" aria-label="Soft-focus grey photograph of a standing figure"></div>
    <div class="card-strip"></div>
    <div class="card-glow"></div>
    <div class="card-details">
      <h1 class="holder-name">TEV</h1>
      <p class="brand-name">Morrowvale</p>
      <ul class="credentials">
        <li>BA (Psych)</li>
        <li>BSc (Hons) Psychology</li>
        <li>Mobile: 0491 627 850</li>
      </ul>
    </div>
    <p class="tagline">Specialising In Psychotherapy</p>
  </article>
</body>
</html>
```